Business Card Design Project

- makeup artist business card

- original and creative

- Elegant design

- Feel free to come out with cool designs but stick to being elegant and attractive

- Design relates to makeup

- includes name, occupation, contact numbers, email, website

- regular size business card

- round corner card

- double sided

- on 1 side it should just have the website name in the center " browsandblush.example "

Industry/Entity Type

Business

Requirements
Must have
• Marla Voss
Makeup Artist
USA: +1 (415)872-6410
Singapore: +65 83027715
marlavoss@browsandblush.example
www.browsandblush.example
Should not have
• nothing cartoon looking.
Pictures of makeup being grab from the internet.. Examples: eyes or lips.

```html
<!DOCTYPE html>
<html lang="en">
<head>
<meta charset="utf-8">
<title>Marla Voss – Makeup Artist Business Card</title>
<link href="https://fonts.googleapis.com/css2?family=Arimo:wght@400;700&family=Tinos:ital,wght@0,700;1,400&display=swap" rel="stylesheet">
<style>
  :root {
    --page-bg: #ece4e8;
    --card-core: #9d2868;
    --card-edge: #761c55;
    --text-light: #f4dbe8;
    --text-white: #ffffff;
    --text-pink: #f07cb8;
    --shine-light: #fbe9f2;
    --shine-mid: #d98ab3;
  }
  html, body {
    margin: 0;
    padding: 0;
    width: 1200px;
    height: 951px;
    overflow: hidden;
    background: var(--page-bg);
  }
  .canvas {
    position: relative;
    width: 1200px;
    height: 951px;
  }
  .card {
    position: absolute;
    width: 640px;
    height: 366px;
    border-radius: 26px;
    background: radial-gradient(ellipse at 50% 50%, var(--card-core) 0%, var(--card-edge) 85%);
    box-shadow: 0 10px 26px rgba(80, 20, 55, 0.25);
    overflow: hidden;
    font-family: "Arimo", Arial, sans-serif;
  }
  .card--front { left: 90px; top: 90px; }
  .card--back { left: 470px; top: 500px; }

  .edge-shine {
    position: absolute;
    top: 0;
    width: 34px;
    height: 100%;
  }
  .edge-shine--left { left: 0; }
  .edge-shine--right { right: 0; }

  .site-mark {
    position: absolute;
    left: 120px;
    top: 166px;
    display: flex;
    align-items: center;
    gap: 14px;
  }
  .site-mark__dots { display: flex; align-items: center; gap: 9px; }
  .dot { background: var(--text-light); border-radius: 50%; }
  .dot--1 { width: 3px; height: 3px; }
  .dot--2 { width: 4px; height: 4px; }
  .dot--3 { width: 5px; height: 5px; }
  .dot--4 { width: 6px; height: 6px; }
  .dot--5 { width: 8px; height: 8px; background: var(--text-white); }
  .site-mark__url {
    color: var(--text-light);
    font-size: 26px;
    letter-spacing: 2.5px;
  }

  .identity {
    position: absolute;
    right: 44px;
    top: 56px;
    text-align: right;
    font-family: "Tinos", "Times New Roman", serif;
  }
  .identity__name {
    color: var(--text-white);
    font-weight: 700;
    font-size: 25px;
  }
  .identity__role {
    color: var(--text-pink);
    font-style: italic;
    font-size: 17px;
    margin-top: 2px;
  }

  .back-url {
    position: absolute;
    left: 40px;
    bottom: 50px;
    color: var(--text-pink);
    font-size: 15px;
  }
  .contact-list {
    position: absolute;
    left: 336px;
    bottom: 34px;
    margin: 0;
    padding: 0;
    list-style: none;
    color: var(--text-white);
    font-size: 15px;
  }
  .contact-list li {
    display: flex;
    align-items: center;
    gap: 9px;
    line-height: 22px;
  }
  .contact-icon { width: 14px; height: 14px; flex: none; }
</style>
</head>
<body>
<main class="canvas">

  <section class="card card--front" aria-label="Business card front">
    <svg class="edge-shine edge-shine--left" viewBox="0 0 34 366" preserveAspectRatio="none" aria-hidden="true">
      <defs>
        <linearGradient id="shineLeft" x1="0" y1="0" x2="1" y2="0">
          <stop offset="0" stop-color="var(--shine-mid)"/>
          <stop offset="0.55" stop-color="var(--shine-light)"/>
          <stop offset="1" stop-color="var(--card-edge)"/>
        </linearGradient>
      </defs>
      <path d="M0 0 H12 Q30 183 12 366 H0 Z" fill="url(#shineLeft)"/>
      <path d="M12 0 Q30 183 12 366" stroke="#ffffff" stroke-width="2" fill="none"/>
    </svg>
    <svg class="edge-shine edge-shine--right" viewBox="0 0 34 366" preserveAspectRatio="none" aria-hidden="true">
      <defs>
        <linearGradient id="shineRight" x1="1" y1="0" x2="0" y2="0">
          <stop offset="0" stop-color="var(--shine-mid)"/>
          <stop offset="0.55" stop-color="var(--shine-light)"/>
          <stop offset="1" stop-color="var(--card-edge)"/>
        </linearGradient>
      </defs>
      <path d="M34 0 H22 Q4 183 22 366 H34 Z" fill="url(#shineRight)"/>
      <path d="M22 0 Q4 183 22 366" stroke="#ffffff" stroke-width="2" fill="none"/>
    </svg>

    <div class="site-mark">
      <div class="site-mark__dots" aria-hidden="true">
        <span class="dot dot--1"></span><span class="dot dot--2"></span><span class="dot dot--3"></span><span class="dot dot--4"></span><span class="dot dot--5"></span>
      </div>
      <span class="site-mark__url">www.browsandblush.example</span>
    </div>
  </section>

  <section class="card card--back" aria-label="Business card back">
    <div class="identity">
      <div class="identity__name">Marla Voss</div>
      <div class="identity__role">Makeup Artist</div>
    </div>

    <div class="back-url">www.browsandblush.example</div>

    <ul class="contact-list">
      <li>
        <svg class="contact-icon" viewBox="0 0 14 14" aria-hidden="true"><circle cx="7" cy="7" r="6.3" fill="none" stroke="#f4dbe8" stroke-width="1.2"/><path d="M5 3.6 L6.3 5.4 L5.6 6.2 Q6.4 7.8 7.9 8.5 L8.7 7.7 L10.4 9 L9.6 10.3 Q6.8 10.2 4.5 7.3 Q3.7 5.3 5 3.6 Z" fill="#f4dbe8"/></svg>
        <span>USA: +1 (415)872-6410</span>
      </li>
      <li>
        <svg class="contact-icon" viewBox="0 0 14 14" aria-hidden="true"><circle cx="7" cy="7" r="6.3" fill="none" stroke="#f4dbe8" stroke-width="1.2"/><path d="M5 3.6 L6.3 5.4 L5.6 6.2 Q6.4 7.8 7.9 8.5 L8.7 7.7 L10.4 9 L9.6 10.3 Q6.8 10.2 4.5 7.3 Q3.7 5.3 5 3.6 Z" fill="#f4dbe8"/></svg>
        <span>Singapore: +65 83027715</span>
      </li>
      <li>
        <svg class="contact-icon" viewBox="0 0 14 14" aria-hidden="true"><rect x="1.5" y="3.5" width="11" height="8" rx="1" fill="#f4dbe8"/><path d="M1.8 3.9 L7 8 L12.2 3.9" stroke="#8a2160" stroke-width="1.1" fill="none"/></svg>
        <span>marlavoss@browsandblush.example</span>
      </li>
    </ul>
  </section>

</main>
</body>
</html>
```